Football/Sports Motivational Poster

Use the picture provided. Crop the lady out to the right. At the top of the poster "Pressure Is A Privilege"
At the bottom of the poster "Prove Them Wrong"
Vertical Poster. Must look Bad Ass! Also include various high res files

```html
<!DOCTYPE html>
<html lang="en">
<head>
<meta charset="utf-8">
<title>Pressure Is A Privilege — Football Poster</title>
<link rel="stylesheet" href="https://fonts.googleapis.com/css2?family=Bebas+Neue&family=Alfa+Slab+One&family=Anton&display=swap">
<style>
  :root {
    --page-bg: #ece8e8;
    --green-bright: #0f7d1c;
    --green-deep: #064a0e;
    --green-dark: #032906;
    --black: #050805;
    --yellow: #e3e61a;
    --yellow-band: #c5cc0a;
    --yellow-ghost: #d4d80e;
    --white: #ffffff;
    --outline-green: #0d6e18;
    --photo-light: #bdbdbd;
    --photo-dark: #3c3c3c;
  }
  html, body {
    margin: 0;
    width: 1200px;
    height: 2400px;
    overflow: hidden;
    background: var(--page-bg);
  }
  .poster {
    position: absolute;
    left: 50px;
    top: 420px;
    width: 1100px;
    height: 1560px;
    box-shadow: 0 14px 30px rgba(0,0,0,0.35);
  }
  .poster svg { display: block; width: 100%; height: 100%; }
  .headline-small {
    font-family: "Bebas Neue", "Anton", sans-serif;
    fill: var(--yellow);
  }
  .headline-big {
    font-family: "Alfa Slab One", serif;
    fill: var(--white);
    stroke: var(--outline-green);
    stroke-width: 6;
    paint-order: stroke fill;
  }
  .tagline-prove {
    font-family: "Anton", "Bebas Neue", sans-serif;
    fill: var(--yellow);
  }
  .tagline-wrong {
    font-family: "Anton", "Bebas Neue", sans-serif;
    fill: var(--white);
  }
</style>
</head>
<body>
<div class="poster">
  <svg viewBox="0 0 790 1120" xmlns="http://www.w3.org/2000/svg">
    <defs>
      <linearGradient id="bg-fade" x1="0" y1="0" x2="0" y2="1">
        <stop offset="0" stop-color="#0f7d1c"/>
        <stop offset="0.45" stop-color="#075212"/>
        <stop offset="0.8" stop-color="#032906"/>
        <stop offset="1" stop-color="#050805"/>
      </linearGradient>
      <linearGradient id="player-tone" x1="0" y1="0" x2="1" y2="1">
        <stop offset="0" stop-color="#d2d2d2"/>
        <stop offset="1" stop-color="#4a4a4a"/>
      </linearGradient>
      <linearGradient id="ghost-tone" x1="0" y1="0" x2="0" y2="1">
        <stop offset="0" stop-color="#d9dc12" stop-opacity="0.4"/>
        <stop offset="0.5" stop-color="#e0e41a" stop-opacity="0.9"/>
        <stop offset="1" stop-color="#c5cc0a" stop-opacity="0.6"/>
      </linearGradient>
    </defs>

    <rect class="poster-bg" width="790" height="1120" fill="url(#bg-fade)"/>

    <g class="diagonal-bands">
      <polygon points="535,0 742,0 330,915 123,915" fill="var(--yellow-band)"/>
      <polygon points="742,0 782,0 370,915 330,915" fill="var(--black)"/>
      <polygon points="782,0 790,0 790,300 440,990 370,990 370,915" fill="var(--yellow-band)"/>
      <polygon points="790,300 790,340 460,1000 420,1000" fill="var(--black)"/>
    </g>

    <rect class="ghost-photo" x="530" y="70" width="260" height="930"
          fill="url(#ghost-tone)" role="img"
          aria-label="Faded yellow-tinted duplicate of the football player walking, helmet in hand"/>

    <rect class="player-photo" x="250" y="100" width="270" height="910" rx="40"
          fill="url(#player-tone)" role="img"
          aria-label="Black and white photo of a football player in a white uniform walking with head down, holding his helmet and a towel"/>

    <text class="headline-small" x="54" y="108" font-size="78" textLength="243" lengthAdjust="spacingAndGlyphs">PRESSURE</text>
    <text class="headline-small" x="54" y="170" font-size="78">IS A</text>

    <text class="headline-big" transform="translate(207,1048) rotate(-90)"
          font-size="205" textLength="865" lengthAdjust="spacingAndGlyphs">PRIVILAGE</text>

    <text class="tagline-prove" x="400" y="1012" font-size="112" textLength="335" lengthAdjust="spacingAndGlyphs">PROVE</text>
    <text class="tagline-wrong" x="395" y="1075" font-size="60" textLength="340" lengthAdjust="spacingAndGlyphs">THEM WRONG</text>
  </svg>
</div>
</body>
</html>
```